Plakat-Design für IT-Systemhaus
brisk IT Solutions suchte ein neues Design in der Kategorie Plakate und hat ein Projekt auf grafikwerkhof.de gestartet.
brisk IT Solutions
The winner of our first design contests on this site. Can only say positive things about them. They work fast, respond in a timely manner and created a great design for us. Overall we're very happy with Quillwick.
Zielgruppe
Wir sind ein IT-Systemhaus mit dem Fokus auf individuelle Cloud Lösungen inkl. bester Kundenbetreuung.
Unsere primäre Zielgruppe sind Unterhnemenskunden, sprich das B2B Geschäft.
Aus der Gruppe der Unternehmenskunden interessieren uns besonders kleine und mittelständische Unternehmen.
Unser Corporate Design ist modern und dennoch auffällig gehalten.
Unsere bevorzugt Schriftart ist 'Ubuntu' bzw. 'Ubuntu Light'.
Unsere Grundfarben sind Orange (#ff8303) Grau (#747474).
Als orientierungshilfe haben wir unser Vorlage für Blöcke und Flyer mit angehangen.
Aufgabenstellung
Es handelt sich um eine Geländerwerbung (doppelseitig) zwischen einer Tankstelle und einer Straße gelegen. (Siehe Anhang)
Die Maße des Anzeitgetafel sind wie folgt: Querformat 135 x 65 (breite x höhe)
Gerne würden wir auf eine etwas provokantere Fragestellung zurückgreifen, um Aufmerksamkeit zu eregen.
Gleichzeitig möchten wir als Lösungsfinder der Fragestellung wargenommen werden.
Gut gefallen hat uns diese Lösung: https://www.grafikwerkhof.at/527190-plakat-fuer-it-systemhaus
Des Weiteren sollte die Anzeige unser Logo, Webadresse sowie unsere Telefonnummer enthalten.
Für Kreative Vorschläge sind wir dankbar.

```html
<!DOCTYPE html>
<html lang="de">
<head>
<meta charset="utf-8">
<title>brisk IT Solutions – Geländerwerbung</title>
<link href="https://fonts.googleapis.com/css2?family=Ubuntu:wght@400;500;700&display=swap" rel="stylesheet">
<style>
  :root {
    --orange: #ff8303;
    --orange-soft: #f39a36;
    --grey-dark: #9a9a9a;
    --white: #ffffff;
    --arch-light: #e2e2e2;
  }
  html, body { margin: 0; padding: 0; overflow: hidden; background: var(--white); }
  .banner {
    position: relative;
    width: 1200px; height: 628px; overflow: hidden;
    background: radial-gradient(ellipse at 45% 35%, #c2c2c2 0%, #aeaeae 55%, var(--grey-dark) 100%);
    font-family: "Ubuntu", sans-serif;
  }
  .decor { position: absolute; inset: 0; width: 1200px; height: 628px; }
  .arch { position: absolute; }
  .arch--left-back { left: 11px; top: 316px; width: 160px; height: 312px; background: var(--arch-light); border-radius: 80px 80px 0 0; }
  .arch--left-front { left: -10px; top: 430px; width: 150px; height: 198px; background: var(--white); border-radius: 75px 75px 0 0; }
  .arch--right-back { left: 1056px; top: 350px; width: 116px; height: 278px; background: var(--arch-light); border-radius: 58px 58px 0 0; }
  .arch--right-front { left: 1034px; top: 446px; width: 110px; height: 182px; background: var(--white); border-radius: 55px 55px 0 0; }
  .cloud-photo {
    position: absolute; left: 112px; top: 88px; width: 308px; height: 540px;
    border-radius: 120px 120px 0 0;
    background: linear-gradient(to bottom,
      var(--orange-soft) 0%, var(--orange-soft) 36%,
      rgba(243,154,54,.75) 40%, rgba(243,154,54,.35) 100%);
  }
  .web-tab {
    position: absolute; left: 55px; top: 410px; width: 66px; height: 218px;
    background: var(--orange-soft); border-radius: 33px 33px 0 0;
  }
  .web-tab span {
    position: absolute; left: 50%; top: 58%;
    transform: translate(-50%, -50%) rotate(-90deg);
    color: var(--white); font-weight: 700; font-size: 26px; white-space: nowrap;
  }
  .headline {
    position: absolute; left: 528px; top: 102px; margin: 0;
    color: var(--orange); font-weight: 500; font-size: 80px; line-height: 74px;
    text-shadow: 2px 3px 4px rgba(0,0,0,.35); white-space: nowrap;
  }
  .headline .line2 { display: block; padding-left: 76px; }
  .subline {
    position: absolute; left: 612px; top: 272px; margin: 0;
    color: var(--white); font-size: 46px; line-height: 45px; font-weight: 400;
    text-shadow: 2px 2px 3px rgba(0,0,0,.35); white-space: nowrap;
  }
  .services { position: absolute; left: 390px; top: 0; margin: 0; padding: 0; list-style: none; }
  .services li {
    position: absolute; left: 0; display: flex; align-items: center; gap: 6px;
    color: var(--white); font-size: 20px; font-weight: 500; white-space: nowrap;
    text-shadow: 1px 1px 2px rgba(0,0,0,.3); transform: translateY(-50%);
  }
  .services svg { width: 36px; height: 36px; fill: none; stroke: var(--white); stroke-width: 1.6; }
  .brand {
    position: absolute; left: 812px; top: 470px;
    color: var(--orange); font-weight: 500; font-size: 30px; white-space: nowrap;
  }
  .contact-bar {
    position: absolute; left: 733px; top: 542px; width: 467px; height: 23px;
    background: var(--orange-soft); border-radius: 12px 0 0 12px;
    color: var(--white); font-size: 13px; font-weight: 500; line-height: 23px;
    padding-left: 36px; box-sizing: border-box; white-space: nowrap;
  }
</style>
</head>
<body>
<div class="banner">
  <div class="arch arch--left-back"></div>
  <div class="arch arch--right-back"></div>

  <svg class="decor" viewBox="0 0 1200 628" aria-hidden="true">
    <g fill="none" stroke="var(--orange)" stroke-linecap="round">
      <path d="M49 0 Q40 110 137 153" stroke-width="7" stroke="var(--orange-soft)"/>
      <path d="M380 142 H526" stroke-width="7" stroke="var(--orange-soft)"/>
      <path d="M1150 218 H1200" stroke-width="7" stroke="var(--orange-soft)"/>
      <path d="M707 386 Q730 480 795 491" stroke-width="8" stroke="var(--orange-soft)"/>
      <path d="M816 110 Q820 40 880 0" stroke-width="1.2"/>
      <path d="M816 110 V88" stroke-width="7"/>
      <path d="M1028 0 Q1030 150 1200 160" stroke-width="1.2"/>
      <path d="M1055 0 Q1040 140 1200 170" stroke-width="1.2"/>
      <path d="M1072 628 V370 Q1072 315 1127 315 Q1183 315 1183 370 V628" stroke-width="1.3"/>
      <path d="M1050 628 V470 Q1050 420 1105 420 Q1161 420 1161 470 V628" stroke-width="1.3"/>
    </g>
    <g fill="none" stroke="var(--white)" stroke-width="1.6">
      <path d="M599 297 H542 Q514 297 514 325"/>
      <path d="M514 521 Q516 553 542 553 H733"/>
    </g>
  </svg>

  <div class="cloud-photo" role="img" aria-label="Orange Wolke mit drei angeschlossenen Netzwerkkabeln"></div>

  <div class="arch arch--left-front"></div>
  <div class="arch arch--right-front"></div>

  <div class="web-tab"><span>brisk-it.de/</span></div>

  <h1 class="headline">»Wer hat wem<span class="line2">was geCloud?«</span></h1>
  <p class="subline">Alles Neuland für Sie?<br>Wir erklären es Ihnen!</p>

  <ul class="services">
    <li style="top:346px">
      <svg viewBox="0 0 36 36"><circle cx="7" cy="20" r="5"/><rect x="22" y="3" width="9" height="9"/><path d="M22 33 L27 25 L32 33 Z"/><path d="M11 17 L22 10 M11 23 L24 29"/></svg>
      IT Infrastruktur
    </li>
    <li style="top:394px">
      <svg viewBox="0 0 36 36"><path d="M18 3 L32 7 V19 Q32 29 18 34 Q4 29 4 19 V7 Z"/><rect x="9" y="13" width="18" height="8" rx="1"/><path d="M12 17 h2 M16 17 h2 M20 17 h2"/></svg>
      IT Sicherheit
    </li>
    <li style="top:455px">
      <svg viewBox="0 0 36 36"><path d="M24 8 H3 V31 H31 V20"/><path d="M3 27 H31"/><circle cx="29" cy="8" r="6"/></svg>
      IT Beratung
    </li>
    <li style="top:510px">
      <svg viewBox="0 0 36 36"><rect x="4" y="11" width="26" height="18"/><path d="M2 32 H33"/><path d="M10 25 L26 6 M24 4 L29 9 M12 24 L9 27"/></svg>
      IT Support
    </li>
  </ul>

  <div class="brand">brisk IT Solutions</div>
  <div class="contact-bar">Lindenallee 12 · 57300 Talbach · Tel.: +49 2700 / 12 34 56 0</div>
</div>
</body>
</html>
```